Generative AI radar Infographics

I want to create an infographic called "Automated Reasoning Horizon Chart for Tender Replies". (see slide 3 of the PowerPoint file). I want to use it on social media (Pellocast and Website). I added 2 inspiration graphics in my brief (see slide 2 of the PowerPoint). I want to add my logo on the infographic. (I also uploaded my company logos). You can find model detailed instructions on slide 1 of the PowerPoint.
Target Market(s)
Business development and sales
Industry/Entity Type
I am a business consultant. I will be using this infographics on Pellocast and in my powerpoint presentations to clients
Look and feel
Each slider illustrates characteristics of the customer's brand and the style your logo design should communicate.

```html
<!DOCTYPE html>
<html lang="en">
<head>
<meta charset="utf-8">
<title>Automated Reasoning Horizon Chart for Tender Replies</title>
<link rel="stylesheet" href="https://fonts.googleapis.com/css2?family=Libre+Baskerville:wght@400;700&family=Arimo:wght@400;700&display=swap">
<style>
  :root {
    --teal: #0893bb;
    --title-teal: #0b93ba;
    --navy: #0b2d42;
    --ink: #111111;
    --label: #1c2a33;
    --ring-1: #e6f3f8;
    --ring-2: #d4eaf2;
    --ring-3: #c1e1ec;
    --ring-4: #aed8e6;
    --ring-5: #9dd0e1;
    --ring-6: #8dc9dc;
    --ring-line: #c9e3ec;
    --paper: #ffffff;
  }
  * { margin: 0; padding: 0; box-sizing: border-box; }
  html, body { width: 1200px; height: 1200px; overflow: hidden; background: var(--paper); }
  .canvas { position: relative; width: 1200px; height: 1200px; background: var(--paper); }

  .chart-title {
    position: absolute; left: 40px; top: 44px;
    font-family: "Libre Baskerville", Georgia, serif;
    font-weight: 700; font-size: 50px; line-height: 63px;
    color: var(--title-teal); letter-spacing: -0.5px;
  }

  .brand {
    position: absolute; left: 790px; top: 60px;
    display: flex; align-items: center; gap: 18px;
    font-family: "Arimo", Arial, sans-serif;
    font-weight: 700; color: var(--navy);
  }
  .brand-mark {
    width: 64px; height: 64px; border-radius: 50%;
    background: var(--navy); flex: none;
  }
  .brand-name { font-size: 34px; line-height: 40px; }

  .radar { position: absolute; left: 0; top: 0; width: 1200px; height: 1200px; }

  .axis-label {
    font-family: "Arimo", Arial, sans-serif; font-weight: 700;
    font-size: 27px; fill: var(--ink); text-anchor: middle;
  }
  .band-label {
    font-family: "Libre Baskerville", Georgia, serif;
    font-size: 25px; fill: var(--paper); letter-spacing: 1px;
  }
  .item-label {
    font-family: "Arimo", Arial, sans-serif; font-size: 16.5px; fill: var(--label);
  }
  .dot-navy { fill: var(--navy); }
  .dot-teal { fill: var(--teal); }
</style>
</head>
<body>
<main class="canvas">
  <h1 class="chart-title">Automated Reasoning<br>Horizon Chart for<br>Tender Replies</h1>

  <div class="brand">
    <span class="brand-mark"></span>
    <span class="brand-name">Marlowe<br>Advisory Group</span>
  </div>

  <svg class="radar" viewBox="0 0 1200 1200" xmlns="http://www.w3.org/2000/svg">
    <defs>
      <path id="arc-decision" d="M 302 725 A 322 322 0 0 1 624 403"/>
      <path id="arc-development" d="M 624 403 A 322 322 0 0 1 946 725"/>
      <path id="arc-capture" d="M 279 725 A 345 345 0 0 0 624 1070"/>
      <path id="arc-strategy" d="M 624 1070 A 345 345 0 0 0 969 725"/>
      <marker id="arrow-head" viewBox="0 0 10 10" refX="8" refY="5" markerWidth="7" markerHeight="7" orient="auto-start-reverse">
        <path d="M0 0 L10 5 L0 10 z" fill="var(--teal)"/>
      </marker>
    </defs>

    <g class="rings" stroke="var(--ring-line)" stroke-width="1">
      <circle cx="624" cy="725" r="312" fill="var(--ring-1)"/>
      <circle cx="620" cy="728" r="256" fill="var(--ring-2)"/>
      <circle cx="620" cy="730" r="212" fill="var(--ring-3)"/>
      <circle cx="620" cy="732" r="164" fill="var(--ring-4)"/>
      <circle cx="620" cy="733" r="112" fill="var(--ring-5)"/>
      <circle cx="620" cy="733" r="69" fill="var(--ring-6)"/>
    </g>

    <g class="bands" fill="none" stroke-width="46">
      <path d="M 290.5 725 A 333.5 333.5 0 0 1 624 391.5" stroke="var(--navy)"/>
      <path d="M 624 391.5 A 333.5 333.5 0 0 1 957.5 725" stroke="var(--teal)"/>
      <path d="M 290.5 725 A 333.5 333.5 0 0 0 624 1058.5" stroke="var(--teal)"/>
      <path d="M 624 1058.5 A 333.5 333.5 0 0 0 957.5 725" stroke="var(--navy)"/>
    </g>

    <g class="band-gaps" stroke="var(--paper)" stroke-width="14">
      <line x1="624" y1="364" x2="624" y2="418"/>
      <line x1="624" y1="1032" x2="624" y2="1086"/>
      <line x1="262" y1="725" x2="316" y2="725"/>
      <line x1="932" y1="725" x2="986" y2="725"/>
    </g>

    <g class="axes" stroke="var(--teal)" stroke-width="1.5">
      <line x1="624" y1="374" x2="624" y2="1076" marker-start="url(#arrow-head)" marker-end="url(#arrow-head)"/>
      <line x1="271" y1="725" x2="977" y2="725" marker-start="url(#arrow-head)" marker-end="url(#arrow-head)"/>
    </g>

    <text class="band-label"><textPath href="#arc-decision" startOffset="50%" text-anchor="middle">DECISION SUPPORT</textPath></text>
    <text class="band-label"><textPath href="#arc-development" startOffset="50%" text-anchor="middle">PROPOSAL DEVELOPMENT</textPath></text>
    <text class="band-label"><textPath href="#arc-capture" startOffset="50%" text-anchor="middle">CAPTURE STRATEGY</textPath></text>
    <text class="band-label"><textPath href="#arc-strategy" startOffset="50%" text-anchor="middle">PROPOSAL STRATEGY</textPath></text>

    <text class="axis-label" x="624" y="318">Process</text>
    <text class="axis-label" x="624" y="350">Enhancement</text>
    <text class="axis-label" x="624" y="1129">Strategy</text>
    <text class="axis-label" x="624" y="1161">Enablement</text>
    <text class="axis-label" x="146" y="673">Insights</text>
    <text class="axis-label" x="146" y="705">Generation</text>
    <text class="axis-label" x="146" y="737">(Trans-formative</text>
    <text class="axis-label" x="146" y="769">Application)</text>
    <text class="axis-label" x="1089" y="704">Task</text>
    <text class="axis-label" x="1089" y="736">Automation</text>
    <text class="axis-label" x="1089" y="769">(Foundational</text>
    <text class="axis-label" x="1089" y="801">Use)</text>

    <g class="quadrant-decision">
      <circle class="dot-navy" cx="576" cy="477" r="7.5"/>
      <text class="item-label" x="598" y="503" text-anchor="end">Bid/No Bid Analysis</text>
      <circle class="dot-navy" cx="407" cy="527" r="7.5"/>
      <text class="item-label" x="420" y="533">Bid Qualification</text>
      <circle class="dot-navy" cx="583" cy="560" r="7.5"/>
      <text class="item-label" x="569" y="566" text-anchor="end">Opportunity assessment</text>
      <circle class="dot-navy" cx="497" cy="591" r="7.5"/>
      <text class="item-label" x="494" y="614" text-anchor="middle">Win Probability modeling</text>
      <circle class="dot-navy" cx="555" cy="647" r="7.5"/>
      <text class="item-label" x="541" y="652" text-anchor="end">Compliance assessment</text>
      <circle class="dot-navy" cx="444" cy="679" r="7.5"/>
      <text class="item-label" x="456" y="703" text-anchor="middle">Strategic Pricing optimization</text>
    </g>

    <g class="quadrant-development">
      <circle class="dot-teal" cx="702" cy="448" r="7.5"/>
      <text class="item-label" x="702" y="475" text-anchor="middle">Company profile</text>
      <circle class="dot-teal" cx="646" cy="498" r="7.5"/>
      <text class="item-label" x="658" y="504">CV and Resumes</text>
      <circle class="dot-teal" cx="830" cy="530" r="7.5"/>
      <text class="item-label" x="818" y="537" text-anchor="end">Past Performance</text>
      <circle class="dot-teal" cx="738" cy="556" r="7.5"/>
      <text class="item-label" x="644" y="578">Due Diligence Questionnaires</text>
      <circle class="dot-teal" cx="650" cy="604" r="7.5"/>
      <text class="item-label" x="663" y="610">Security Questionnaires</text>
      <circle class="dot-teal" cx="901" cy="633" r="7.5"/>
      <text class="item-label" x="889" y="639" text-anchor="end">Technical solution</text>
      <circle class="dot-teal" cx="702" cy="659" r="7.5"/>
      <text class="item-label" x="714" y="665">Statement of Work</text>
      <circle class="dot-teal" cx="646" cy="684" r="7.5"/>
      <text class="item-label" x="658" y="690">Compliance Matrix</text>
      <circle class="dot-teal" cx="850" cy="694" r="7.5"/>
      <text class="item-label" x="779" y="715">Executive Summary</text>
    </g>

    <g class="quadrant-capture">
      <circle class="dot-teal" cx="564" cy="758" r="7.5"/>
      <text class="item-label" x="550" y="764" text-anchor="end">Customer Hot Buttons</text>
      <circle class="dot-teal" cx="361" cy="795" r="7.5"/>
      <text class="item-label" x="374" y="801">SWOT Analysis</text>
      <circle class="dot-teal" cx="601" cy="828" r="7.5"/>
      <text class="item-label" x="584" y="833" text-anchor="end">Capture Plan</text>
      <circle class="dot-teal" cx="453" cy="850" r="7.5"/>
      <text class="item-label" x="481" y="877" text-anchor="middle">Customer Intelligence</text>
      <circle class="dot-teal" cx="394" cy="909" r="7.5"/>
      <text class="item-label" x="406" y="915">Competitive Intelligence</text>
      <circle class="dot-teal" cx="589" cy="953" r="7.5"/>
      <text class="item-label" x="575" y="960" text-anchor="end">Value Proposition</text>
    </g>

    <g class="quadrant-strategy">
      <circle class="dot-navy" cx="832" cy="751" r="7.5"/>
      <text class="item-label" x="831" y="778" text-anchor="middle">Proposal outline</text>
      <circle class="dot-navy" cx="666" cy="798" r="7.5"/>
      <text class="item-label" x="678" y="804">Proposal plan</text>
      <circle class="dot-navy" cx="768" cy="830" r="7.5"/>
      <text class="item-label" x="781" y="836">Differentiators</text>
      <circle class="dot-navy" cx="789" cy="869" r="7.5"/>
      <text class="item-label" x="775" y="891" text-anchor="middle">Win Theme extraction</text>
      <circle class="dot-navy" cx="643" cy="933" r="7.5"/>
      <text class="item-label" x="655" y="939">Key messages extraction</text>
    </g>
  </svg>
</main>
</body>
</html>
```